Stationery and Logo Design Project for new NZ Accounting Firm

Our company name is based in Auckland, New Zealand and is called TMV CA Limited. We are a chartered accountancy firm hence the CA abbreviations.

We need a full logo stationery design: Logo, Letterhead, Business Card and Compliments slip.

We are looking for a bold, modern and clean/simple design that makes us stand out. We want to stand out as professionals in the industry and would like the logo and stationery that our clients see to convey this image. We also want to break away from the traditional boring views of book/bean accountants. We are not doing the same old things others are doing and are mainly cloud based but with face to face business relationship focused as well.

We see ourselves as business advisers that provide more than just filing their tax returns. We want to add value to their business and be a partner in their business ventures.

We want the logo to convey the above and also attract potential clients when they see our ads among the thousands on zarvo and the tallow index.

The logo can be for the "TMV" with CA Ltd seperately or a logo/design beside the TMV. But open to other suggestions or concept.

Hi Designers

The designs I have received so far is not quite what I want.

I want something modern and bold that is DIFFERENT from others, from the usual logo designs. Some logo that when people look at it they will remember it as opposed to fading in the background of other competitors' logo.

Lower case lettering for the TMV could be something to explore as I have not seen a lot of these and they do appeal to me.

Thanks

We can focus on the logo first as that will form the main part for all stationery.

Reason: Final stages of choosing a logo design so need to time for designers to submit the letterhead, namecards designs.

Target Market(s)

Our target clients are small to medium business ranging from the sole trader to 50 employees businesses

Industry/Entity Type

Business

```html
<!DOCTYPE html>
<html lang="en">
<head>
<meta charset="utf-8">
<title>TMV CA Ltd — Business Card</title>
<link rel="stylesheet" href="https://fonts.googleapis.com/css2?family=Open+Sans:wght@400;600;700;800&display=swap">
<style>
  :root {
    --backdrop: #1d1d1f;
    --card: #ffffff;
    --navy: #1f3566;
    --red: #c0202b;
    --red-soft: #e6a3a8;
    --grey-text: #555a61;
    --black: #0d0d0d;
  }
  * { box-sizing: border-box; margin: 0; padding: 0; }
  html, body {
    width: 1200px; height: 765px; overflow: hidden;
    background: var(--backdrop);
    font-family: "Open Sans", Arial, sans-serif;
  }
  .canvas {
    position: relative; width: 1200px; height: 765px;
    display: flex; align-items: center; justify-content: center; gap: 44px;
  }
  .card {
    position: relative; width: 540px; height: 320px;
    background: var(--card); border-radius: 22px; overflow: hidden;
  }

  /* Front */
  .card-front .holder {
    position: absolute; top: 38px; width: 100%; text-align: center;
    font-size: 20px; font-weight: 700; color: var(--navy); letter-spacing: .3px;
  }
  .card-front .holder .title { font-weight: 400; color: var(--red); }
  .rule {
    position: absolute; left: 0; width: 100%; height: 2px;
    background: linear-gradient(90deg, rgba(192,32,43,.1), var(--red) 50%, rgba(192,32,43,.1));
  }
  .rule-top { top: 78px; }
  .rule-bottom { top: 206px; }
  .wordmark {
    position: absolute; top: 104px; width: 100%; text-align: center;
    font-size: 62px; font-weight: 700; color: var(--navy); line-height: 1;
    letter-spacing: 1px;
  }
  .contacts {
    position: absolute; top: 222px; width: 100%;
    display: flex; flex-direction: column; align-items: center; gap: 4px;
    font-size: 13px; color: var(--grey-text);
  }
  .contacts .row { display: flex; gap: 12px; align-items: center; }
  .contacts .item { display: inline-flex; align-items: center; gap: 4px; }
  .contacts svg { width: 11px; height: 11px; fill: var(--navy); }
  .contacts .address { letter-spacing: 1px; font-size: 13.5px; }

  /* Back */
  .card-back .mark {
    position: absolute; top: 70px; width: 100%; text-align: center;
    font-size: 120px; font-weight: 800; color: var(--black); line-height: 1;
    letter-spacing: -2px;
  }
  .card-back .web {
    position: absolute; top: 228px; width: 100%; text-align: center;
    font-size: 28px; font-weight: 400; color: var(--navy);
  }
</style>
</head>
<body>
<main class="canvas">
  <section class="card card-front" aria-label="Business card front">
    <p class="holder">Your Name, <span class="title">Title</span></p>
    <div class="rule rule-top"></div>
    <p class="wordmark">TMV CA LTD</p>
    <div class="rule rule-bottom"></div>
    <div class="contacts">
      <div class="row">
        <span class="item"><svg viewBox="0 0 12 12"><path d="M3 1l2 2.5-1.2 1.2a7 7 0 0 0 3.5 3.5L8.5 7 11 9l-1.5 2C5 11 1 7 1 2.5z"/></svg>123-456-789</span>
        <span class="item"><svg viewBox="0 0 12 12"><rect x="3" y="0.5" width="6" height="11" rx="1"/><rect x="4" y="2" width="4" height="6" fill="#fff"/></svg>123-456-789</span>
      </div>
      <div class="row">
        <span class="item"><svg viewBox="0 0 12 12"><rect x="0.5" y="2.5" width="11" height="7" rx="1"/><path d="M1 3l5 3.5L11 3" stroke="#fff" stroke-width="1" fill="none"/></svg>info@tmvmail.com</span>
        <span class="item"><svg viewBox="0 0 12 12"><circle cx="6" cy="6" r="5.5"/></svg>www.website.com</span>
      </div>
      <p class="address">00, Street name, City, State 0032</p>
    </div>
  </section>

  <section class="card card-back" aria-label="Business card back">
    <p class="mark">TMV</p>
    <p class="web">www.website.com</p>
  </section>
</main>
</body>
</html>
```